Website design for a construction company

The logo and the copies of all the 3 pages are attached below. I don't have a preference in colors but I would ideally like to use the colors on my logo, dark teal (secondary) and copper (primary).

Company Name: Corvel Group

Location: London, UK

Business Overview:

Corvel Group is a comprehensive construction company based in London, specializing in a wide range of construction services. We cater to various sectors, providing services including electrical work, painting and decorating, plastering, plumbing, carpentry, kitchen and bathroom installations, loft conversions, and extensions. Our team is known for its skilled craftsmanship, attention to detail, and commitment to quality.

What "CORVEL" stands for:

Our company name, 'CORVEL', is derived from Corvelion, the ancient Greek god of craftsmen, blacksmiths, artisans, sculptors, metals, metallurgy, fire, and volcanoes. Corvelion was renowned in mythology for his incredible skill in crafting and creating, making him the patron of all craftsmen and artisans. His name is synonymous with the mastery of artisanship and the creation of wondrous, enduring works.

In choosing 'CORVEL' as our name, we embody the spirit and skills of Corvelion. It reflects our commitment to craftsmanship, excellence, and durability in the field of construction. Just as Corvelion was known for his meticulous work, precision, and innovative creations, our company strives to uphold these qualities in every project we undertake.

Our name is a constant reminder of our dedication to quality, innovation, and the art of building. It symbolizes our endeavor to achieve the highest standards in construction, much like Corvelion did in his timeless creations. In essence, 'CORVEL' is not just our name; it's a representation of our ethos and the high standards we set for ourselves in the construction industry.

Target Audience:

Our primary audience includes homeowners, real estate developers, and commercial clients in London seeking reliable, high-quality construction services.

Unique Selling Points:

Diverse Range of Services: Offering a one-stop solution for all construction needs.

Certified and Experienced: Professional team with a strong focus on delivering certified and compliant work, particularly in electrical services.

Client-Centric Approach: Emphasizing client satisfaction, we tailor our services to meet the unique needs and visions of our clients.

Quality and Reliability: Commitment to high-quality materials, skilled workmanship, and delivering projects on time and within budget.

Website Requirements:

Clean, professional design reflecting the quality and reliability of our services.

User-friendly navigation to easily access information about our services, portfolio, company background, and contact details.

Portfolio section showcasing our past projects with placeholders for images and descriptions.

Integration of a contact form, map for our location, and links to our social media accounts.

Mobile-responsive design to ensure accessibility across various devices.

Purpose of the Website:
The website aims to:

Establish an online presence and credibility in the construction industry.

Provide an informative resource about our services and past projects to potential clients.

Facilitate easy communication and inquiries through an integrated contact system.

Tone and Style:

Professional, informative, and welcoming. The website should convey trustworthiness and expertise in the construction field.

Target Market(s)

homeowners, real estate developers, and commercial clients

Industry/Entity Type

Construction

Number of Pages Required

3 page

Colors

Designer to choose colors to be used in the design.

```html
<!DOCTYPE html>
<html lang="en">
<head>
<meta charset="utf-8">
<title>Corvel Group — Construction in London</title>
<link href="https://fonts.googleapis.com/css2?family=Lato:wght@300;400;700;900&family=Roboto:wght@400;500;700&display=swap" rel="stylesheet">
<style>
:root{
  --teal:#16918a;
  --teal-dark:#0f7a73;
  --copper:#b5843f;
  --copper-dark:#a07030;
  --ink:#1d1d1f;
  --text:#666;
  --footer:#2a2a2c;
  --orange:#f26a1b;
  --white:#fff;
}
*{margin:0;padding:0;box-sizing:border-box}
html,body{width:1200px;height:3939px;overflow:hidden}
body{position:relative;font-family:"Roboto",sans-serif;color:var(--ink);background:var(--white)}
.abs{position:absolute}
h1,h2,h3{font-family:"Lato",sans-serif}
.btn{position:absolute;display:flex;align-items:center;justify-content:center;gap:8px;background:var(--copper);color:#fff;font-family:"Roboto",sans-serif;font-weight:700;font-size:14px;letter-spacing:.3px;border-radius:2px;box-shadow:0 3px 6px rgba(0,0,0,.15)}
.btn .arr{width:15px;height:15px;border-radius:50%;background:#fff;display:inline-flex;align-items:center;justify-content:center}

/* top bar */
.topbar{left:0;top:0;width:1200px;height:42px;background:var(--teal);color:#fff;font-size:14px}
.topbar .copper{position:absolute;right:0;top:0;width:250px;height:42px;background:var(--copper);clip-path:polygon(28px 0,100% 0,100% 100%,0 100%)}
.topbar .item{position:absolute;top:12px;display:flex;align-items:center;gap:7px;font-weight:500}
.topbar .sep{position:absolute;top:9px;width:1px;height:25px;background:rgba(255,255,255,.5)}
.topbar .social{position:absolute;top:15px;width:12px;height:12px;border-radius:50%;background:#fff}

/* header */
.header{left:0;top:42px;width:1200px;height:76px;background:#fff}
.brand{display:flex;align-items:center;gap:8px;font-family:"Lato",sans-serif;font-weight:400;white-space:nowrap;text-transform:uppercase}
.brand .mark{width:34px;height:34px;background:var(--copper);flex:none}
.header .brand{position:absolute;left:110px;top:20px;font-size:23px;letter-spacing:.3px;color:var(--ink)}
.nav a{position:absolute;top:28px;font-size:15px;font-weight:500;color:var(--ink);text-decoration:none}
.nav a.active{color:var(--copper)}
.nav a.active::after{content:"";position:absolute;left:-2px;right:-2px;bottom:-8px;height:2px;background:var(--copper)}

/* hero */
.hero{left:0;top:118px;width:1200px;height:677px;background:var(--teal);clip-path:polygon(0 0,100% 0,100% 566px,50% 677px,0 566px)}
.hero .photo{position:absolute;inset:0;background:linear-gradient(180deg,#6b6f78 0%,#4b4f5a 22%,#2f3a4c 48%,#3a3338 70%,#1e2332 100%);clip-path:polygon(0 0,100% 0,100% 566px,50% 639px,0 566px)}
.hero .photo::after{content:"";position:absolute;inset:0;background:radial-gradient(ellipse at 50% 78%,rgba(214,150,80,.35),transparent 55%)}
.hero h1{position:absolute;left:0;width:1200px;top:207px;text-align:center;color:#fff;font-size:50px;line-height:52px;font-weight:400}
.hero h1 b{font-weight:700}
.hero p{position:absolute;left:0;width:1200px;top:332px;text-align:center;color:#fff;font-size:17px;font-weight:500}

/* welcome */
.hexphoto{left:138px;top:844px;width:445px;height:512px;clip-path:polygon(50% 0,100% 25%,100% 75%,50% 100%,0 75%,0 25%);background:linear-gradient(160deg,#d8d4cc 0%,#efece6 35%,#c9a46a 55%,#f4f2ee 70%,#1f2e52 100%)}
.welcome h2{left:665px;top:940px;width:440px;font-size:35px;line-height:46px;font-weight:400}
.welcome h2 b{font-weight:700}
.welcome p{position:absolute;left:666px;width:422px;font-size:14px;line-height:24px;color:var(--text);text-align:justify}

/* why choose */
.why{left:0;top:1463px;width:1200px;height:372px;background:var(--copper)}
.why h2{position:absolute;left:0;width:1200px;top:60px;text-align:center;color:#fff;font-size:40px;font-weight:400}
.why h2 b{font-weight:700}
.why .rule{position:absolute;left:552px;top:117px;width:96px;height:4px;background:var(--teal)}
.worker{left:940px;top:1399px;width:260px;height:436px;background:linear-gradient(180deg,#2f8fd6 0%,#2f8fd6 8%,#e8b48e 14%,#d99a72 24%,#f3a13a 34%,#ef8a1f 70%,#7e8794 100%);border-radius:120px 0 0 0;opacity:.95}
.card{position:absolute;top:1688px;width:311px;height:292px;background:#fff;box-shadow:0 6px 16px rgba(0,0,0,.12);border-bottom:5px solid var(--copper);text-align:center}
.card h3{margin-top:70px;font-family:"Roboto",sans-serif;font-size:18px;font-weight:700}
.card p{margin:22px 25px 0;font-size:15px;line-height:25px;color:var(--text);text-align:justify;text-align-last:center}
.hexicon{position:absolute;top:1633px;width:94px;height:107px;background:var(--teal);clip-path:polygon(50% 0,100% 25%,100% 75%,50% 100%,0 75%,0 25%);display:flex;align-items:center;justify-content:center}

/* services */
.sec-title{position:absolute;left:0;width:1200px;text-align:center;font-size:36px;font-weight:400}
.sec-title b{font-weight:700}
.sec-lead{position:absolute;left:270px;width:660px;text-align:center;font-size:14px;line-height:23px;color:var(--text)}
.svc{position:absolute;width:233px;height:243px;background:#fff;border-radius:6px;box-shadow:0 2px 12px rgba(0,0,0,.1)}
.svc .ph{position:absolute;left:9px;top:9px;width:215px;height:180px}
.svc span{position:absolute;left:0;width:233px;top:208px;text-align:center;font-size:15px;font-weight:500}

/* testimonials */
.tcard{position:absolute;top:3007px;width:407px;height:230px;background:#fff;border-radius:40px;box-shadow:0 6px 14px rgba(0,0,0,.25)}
.tcard .q{position:absolute;left:100px;top:18px;font-family:"Lato",sans-serif;font-weight:900;font-size:64px;color:var(--orange);line-height:64px}
.tcard p{position:absolute;left:100px;top:82px;width:272px;font-size:14px;line-height:24px;color:var(--text)}
.tcard .name{position:absolute;left:100px;top:163px;font-size:16px;font-weight:500}
.tcard .stars{position:absolute;left:100px;top:184px;font-size:17px;line-height:18px;color:var(--orange);letter-spacing:2px}
.avatar{position:absolute;top:3065px;width:115px;height:115px;border-radius:50%;background:linear-gradient(180deg,#c9ced4,#6f7782);box-shadow:0 3px 8px rgba(0,0,0,.2)}

/* cta */
.cta{left:0;top:3315px;width:1200px;height:272px;background:var(--teal);color:#fff;text-align:center}
.cta h2{position:absolute;left:0;width:1200px;top:38px;font-size:38px;font-weight:400}
.cta h2 b{font-weight:700}
.cta p{position:absolute;left:280px;width:640px;top:110px;font-size:14px;line-height:23px}

/* footer */
.footer{left:0;top:3587px;width:1200px;height:352px;background:var(--footer);color:#fff}
.footer .brand{position:absolute;left:115px;top:95px;font-size:25px;letter-spacing:.3px;color:#fff}
.footer .ring{position:absolute;top:180px;width:27px;height:27px;border:2px solid #fff;border-radius:50%}
.footer h4{position:absolute;top:67px;font-size:16px;font-weight:700}
.footer ul{position:absolute;top:113px;list-style:none;font-size:13px;line-height:25.5px}
.footer .ci{position:absolute;left:813px;font-size:13px;line-height:20px}
.footer .ci b{display:block;font-size:11px}
.footer .ci svg{position:absolute;left:0;top:2px}
.footer .ci div{margin-left:22px}
.footer .rule{position:absolute;left:110px;width:980px;top:281px;height:1px;background:#4a4a4d}
.footer .copy{position:absolute;left:0;width:1200px;top:307px;text-align:center;font-size:14px}
.totop{position:absolute;left:1105px;top:263px;width:37px;height:37px;border-radius:50%;background:var(--copper);display:flex;align-items:center;justify-content:center}
</style>
</head>
<body>

<!-- top bar -->
<div class="abs topbar">
  <div class="copper"></div>
  <div class="item" style="left:110px">
    <svg width="11" height="11" viewBox="0 0 24 24"><path fill="#fff" d="M6.6 10.8a15 15 0 0 0 6.6 6.6l2.2-2.2c.3-.3.7-.4 1-.2 1.1.4 2.3.6 3.6.6.6 0 1 .4 1 1V20c0 .6-.4 1-1 1A17 17 0 0 1 3 4c0-.6.4-1 1-1h3.5c.6 0 1 .4 1 1 0 1.3.2 2.5.6 3.6.1.3 0 .7-.2 1z"/></svg>
    +44 20 7946 0321</div>
  <div class="sep" style="left:271px"></div>
  <div class="item" style="left:305px">
    <svg width="12" height="10" viewBox="0 0 24 18"><rect width="24" height="18" rx="2" fill="#fff"/><path d="M1 2l11 8 11-8" stroke="#16918a" stroke-width="2" fill="none"/></svg>
    info@corvelbuild.co.uk</div>
  <div class="sep" style="left:495px"></div>
  <div class="item" style="left:524px">
    <svg width="12" height="12" viewBox="0 0 24 24"><circle cx="12" cy="12" r="10" stroke="#fff" stroke-width="2.5" fill="none"/><path d="M12 6v6l4 2" stroke="#fff" stroke-width="2.5" fill="none"/></svg>
    24 Hour Emergency Service Available</div>
  <span class="social" aria-label="Social link" style="left:1004px"></span>
  <span class="social" aria-label="Social link" style="left:1039px"></span>
  <span class="social" aria-label="Social link" style="left:1075px"></span>
</div>

<!-- header -->
<header class="abs header">
  <div class="brand"><span class="mark"></span>Corvel Group</div>
  <nav class="nav">
    <a class="active" style="left:376px">Home</a>
    <a style="left:442px">About Us</a>
    <a style="left:529px">Our Services</a>
    <a style="left:639px">Our Projects</a>
    <a style="left:748px">Contact Us</a>
  </nav>
  <div class="btn" style="left:962px;top:19px;width:127px;height:38px">Get A Quote</div>
</header>

<!-- hero -->
<section class="abs hero">
  <div class="photo" role="img" aria-label="Aerial view of London at dusk with the river and Tower Bridge lit up"></div>
  <h1><b>BUILDING YOUR DREAMS</b><br>INTO REALITY</h1>
  <p>Expert Craftsmanship Meets Unmatched Reliability in the Heart of London</p>
  <div class="btn" style="left:509px;top:389px;width:184px;height:53px">GET STARTED
    <span class="arr"><svg width="8" height="8" viewBox="0 0 10 10"><path d="M3 1l4 4-4 4" stroke="#b5843f" stroke-width="2" fill="none"/></svg></span></div>
</section>

<!-- welcome -->
<section class="welcome">
  <div class="abs hexphoto" role="img" aria-label="Bright modern kitchen with white cabinets, brass fittings and a navy island"></div>
  <h2 class="abs"><b>WELCOME TO</b> CORVEL GROUP</h2>
  <p style="top:1055px">Where Construction Meets Excellence. Based in London, we are committed to transforming your spaces into exceptional places.</p>
  <p style="top:1114px">Our team is dedicated to delivering the highest quality in every project, attending to every detail with precision and care.</p>
  <div class="btn" style="left:667px;top:1200px;width:159px;height:48px">LEARN MORE
    <span class="arr"><svg width="8" height="8" viewBox="0 0 10 10"><path d="M3 1l4 4-4 4" stroke="#b5843f" stroke-width="2" fill="none"/></svg></span></div>
</section>

<!-- why choose us -->
<section class="abs why">
  <h2><b>WHY CHOOSE</b> US</h2>
  <div class="rule"></div>
</section>
<div class="abs worker" role="img" aria-label="Smiling builder in a blue hard hat and orange hi-vis vest giving a thumbs up"></div>

<div class="card" style="left:112px"><h3>Our Expertise</h3><p>Leveraging over 10 years of experience, Corvel Group stands as a beacon of excellence in the construction industry. We handle each project, big or small, with unmatched professionalism and skill.</p></div>
<div class="card" style="left:445px"><h3>Quality Assurance</h3><p>Quality is not just a promise, but a practice. Meticulous attention to detail ensures flawless finishes and durable structures, bringing long-lasting satisfaction to our clients.</p></div>
<div class="card" style="left:778px"><h3>Certified Excellence</h3><p>Your safety and satisfaction are our top priorities. We provide electrical certificates and adhere to the highest industry standards, offering peace of mind in every service.</p></div>

<div class="hexicon" style="left:220px"><svg width="46" height="46" viewBox="0 0 48 48" fill="none" stroke="#fff" stroke-width="2"><circle cx="24" cy="14" r="6"/><path d="M14 34c2-7 6-10 10-10s8 3 10 10"/><path d="M6 28l8 8 6-2M42 28l-8 8-6-2"/></svg></div>
<div class="hexicon" style="left:553px"><svg width="46" height="46" viewBox="0 0 48 48" fill="none" stroke="#fff" stroke-width="2"><circle cx="24" cy="16" r="9"/><path d="M20 16l3 3 5-6"/><path d="M8 30c4 0 8 6 12 6h8M40 30c-4 0-8 6-12 6M6 26v14M42 26v14"/></svg></div>
<div class="hexicon" style="left:886px"><svg width="46" height="46" viewBox="0 0 48 48" fill="none" stroke="#fff" stroke-width="2"><rect x="10" y="8" width="24" height="30" rx="2"/><path d="M15 16h14M15 21h14M15 26h8"/><circle cx="33" cy="32" r="6"/><path d="M30 37l-1 6 4-2 4 2-1-6"/></svg></div>

<!-- services -->
<h2 class="sec-title" style="top:2048px"><b>OUR</b> SERVICES</h2>
<p class="sec-lead" style="top:2110px">Tailored to Your Needs. Discover how we can bring your vision to life, covering every aspect of construction from the initial design to the final touches.</p>

<div class="svc" style="left:102px;top:2197px"><div class="ph" role="img" aria-label="Electricians in hard hats working at a fuse panel" style="background:linear-gradient(135deg,#6b6a5a,#c9b860,#4a5a6a)"></div><span>Electrical Work</span></div>
<div class="svc" style="left:356px;top:2197px"><div class="ph" role="img" aria-label="Decorators painting a wall in navy blue" style="background:linear-gradient(135deg,#e6e2dc,#cfc6b8,#2c4478)"></div><span>Painting and Decorating</span></div>
<div class="svc" style="left:610px;top:2197px"><div class="ph" role="img" aria-label="Plasterer working under a skylight beside a ladder" style="background:linear-gradient(135deg,#d9d9d9,#aeb2b5,#8a8e92)"></div><span>Plastering</span></div>
<div class="svc" style="left:864px;top:2197px"><div class="ph" role="img" aria-label="Plumber fixing pipes under a sink" style="background:linear-gradient(135deg,#3f6fb5,#d4d7db,#2a4d86)"></div><span>Plumbing</span></div>
<div class="svc" style="left:102px;top:2465px"><div class="ph" role="img" aria-label="Carpenter measuring timber boards in a workshop" style="background:linear-gradient(135deg,#8a7458,#cdb793,#4e4338)"></div><span>Carpentry</span></div>
<div class="svc" style="left:356px;top:2465px"><div class="ph" role="img" aria-label="Modern bathroom with round mirror and freestanding tub" style="background:linear-gradient(135deg,#6d6a67,#b9b4ad,#e8e5e0)"></div><span>Kitchen &amp; Bath Installations</span></div>
<div class="svc" style="left:610px;top:2465px"><div class="ph" role="img" aria-label="Converted loft living room with sloped skylights" style="background:linear-gradient(135deg,#f0ede8,#c9c2b8,#7d6a55)"></div><span>Loft Conversions</span></div>
<div class="svc" style="left:864px;top:2465px"><div class="ph" role="img" aria-label="House extension frame with scaffolding under a blue sky" style="background:linear-gradient(135deg,#9fb2c8,#d8c4a0,#8a6a45)"></div><span>Extensions</span></div>

<!-- testimonials -->
<h2 class="sec-title" style="top:2850px;font-size:42px"><b>OUR SATISFIED</b> CLIENTS</h2>
<p class="sec-lead" style="top:2917px;left:260px;width:680px">Our commitment to excellence has earned us the trust of numerous homeowners and businesses in London. Read their stories and understand the Corvel Group difference.</p>

<svg class="abs" style="left:42px;top:3105px" width="24" height="38" viewBox="0 0 24 38"><path d="M20 3L5 19l15 16" stroke="#888" stroke-width="4" fill="none"/></svg>
<svg class="abs" style="left:1135px;top:3105px" width="24" height="38" viewBox="0 0 24 38"><path d="M4 3l15 16L4 35" stroke="#888" stroke-width="4" fill="none"/></svg>

<div class="tcard" style="left:179px"><div class="q">“</div><p>Sed ut perspiciatis unde omnis iste natus sit voluptatem accusantium doloremque laudantium, totam rem aperiam,</p><div class="name">Daniel Marsh</div><div class="stars">★★★★★</div></div>
<div class="avatar" style="left:125px" role="img" aria-label="Client portrait"></div>
<div class="tcard" style="left:668px"><div class="q">“</div><p>Sed ut perspiciatis unde omnis iste natus sit voluptatem accusantium doloremque laudantium, totam rem aperiam,</p><div class="name">Daniel Marsh</div><div class="stars">★★★★★</div></div>
<div class="avatar" style="left:614px" role="img" aria-label="Client portrait"></div>

<!-- call to action -->
<section class="abs cta">
  <h2><b>READY TO START</b> YOUR PROJECT?</h2>
  <p>Contact us today for a consultation and embark on the journey to turn your construction dreams into a stunning reality.</p>
  <div class="btn" style="left:521px;top:176px;width:158px;height:46px">CONTACT US
    <span class="arr"><svg width="8" height="8" viewBox="0 0 10 10"><path d="M3 1l4 4-4 4" stroke="#b5843f" stroke-width="2" fill="none"/></svg></span></div>
</section>

<!-- footer -->
<footer class="abs footer">
  <div class="brand"><span class="mark"></span>Corvel Group</div>
  <span class="ring" aria-label="Social link" style="left:165px"></span>
  <span class="ring" aria-label="Social link" style="left:201px"></span>
  <span class="ring" aria-label="Social link" style="left:238px"></span>
  <span class="ring" aria-label="Social link" style="left:274px"></span>

  <h4 style="left:437px">Quick Links</h4>
  <ul style="left:437px"><li>About Us</li><li>Services</li><li>Projects</li><li>Contact Us</li></ul>
  <h4 style="left:605px">About Company</h4>
  <ul style="left:605px"><li>Support</li><li>Terms &amp; Condition</li><li>Contact Us</li><li>Privacy Policy</li><li>FAQ</li></ul>
  <h4 style="left:813px">Contact Us</h4>
  <div class="ci" style="top:109px"><svg width="12" height="12" viewBox="0 0 24 24"><path fill="#b5843f" d="M6.6 10.8a15 15 0 0 0 6.6 6.6l2.2-2.2c.3-.3.7-.4 1-.2 1.1.4 2.3.6 3.6.6.6 0 1 .4 1 1V20c0 .6-.4 1-1 1A17 17 0 0 1 3 4c0-.6.4-1 1-1h3.5c.6 0 1 .4 1 1 0 1.3.2 2.5.6 3.6.1.3 0 .7-.2 1z"/></svg><div><b>Phone</b>+44 20 7946 0321</div></div>
  <div class="ci" style="top:160px"><svg width="13" height="10" viewBox="0 0 24 18"><rect width="24" height="18" rx="2" fill="#b5843f"/><path d="M1 2l11 8 11-8" stroke="#2a2a2c" stroke-width="2" fill="none"/></svg><div><b>Email</b>info@corvelgroup.co.uk</div></div>
  <div class="ci" style="top:212px"><svg width="11" height="14" viewBox="0 0 20 26"><path fill="#b5843f" d="M10 0a10 10 0 0 0-10 10c0 7 10 16 10 16s10-9 10-16A10 10 0 0 0 10 0zm0 14a4 4 0 1 1 0-8 4 4 0 0 1 0 8z"/></svg><div><b>Location</b>48 Harrow Lane, Southwark, London SE1 4QT</div></div>

  <div class="totop"><svg width="14" height="14" viewBox="0 0 14 14"><path d="M2 10l5-5 5 5" stroke="#fff" stroke-width="2" fill="none"/></svg></div>
  <div class="rule"></div>
  <div class="copy">2024 Copyright - &nbsp;Corvel Group &nbsp;| All Rights Reserved</div>
</footer>

</body>
</html>
```